Summer Drinks Flyer for Coffee Shop

We are a coffee shop in London and would like to have a cool and nice flyer for our summer drinks (juices and frozen drink) flyer - see on the attached file for the list

Attached you can find an "attempt" - please note that I would no necessary need the image below.

I also attache our new logo.

thank you

```html
<!DOCTYPE html>
<html lang="en">
<head>
<meta charset="utf-8">
<title>Summer Drinks Flyer</title>
<link href="https://fonts.googleapis.com/css2?family=Allura&family=Alice&display=swap" rel="stylesheet">
<style>
  :root {
    --gold: #b8902b;
    --white: #ffffff;
    --ink: #111111;
    --panel-black: #0c0c0c;
    --accent-yellow: #f2c94c;
  }
  * { margin: 0; padding: 0; box-sizing: border-box; }
  html, body { width: 848px; height: 1200px; overflow: hidden; background: var(--white); }
  .flyer { position: relative; width: 848px; height: 1200px; overflow: hidden; font-family: "Alice", Georgia, serif; }
  .quad { position: absolute; width: 424px; height: 600px; z-index: 0; }
  .quad--tl { left: 0; top: 0; background: var(--white); }
  .quad--tr { left: 424px; top: 0; background: var(--gold); }
  .quad--bl { left: 0; top: 600px; background: var(--gold); }
  .quad--br { left: 424px; top: 600px; background: var(--white); }

  .photo { position: absolute; z-index: 1; }
  .title, .heading, .menu, .price-badge, .offer, .brand { z-index: 2; }

  .title { position: absolute; top: 4px; font-family: "Allura", cursive; font-size: 64px; line-height: 1; }
  .title--dark { right: 432px; color: var(--ink); }
  .title--light { left: 434px; color: var(--white); }

  .heading { position: absolute; font-size: 28px; line-height: 1; }
  .heading--dark { color: var(--ink); }
  .heading--light { color: var(--white); }

  .menu { position: absolute; list-style: none; font-size: 20px; line-height: 35.5px; }
  .menu--dark { color: var(--ink); }
  .menu--light { color: var(--white); }

  .price-badge { position: absolute; width: 86px; height: 86px; }
  .price-badge svg { position: absolute; inset: 0; }
  .price-badge span { position: absolute; inset: 0; display: flex; align-items: center; justify-content: center; font-size: 24px; }
  .price-badge--gold span { color: var(--white); }
  .price-badge--white span { color: var(--ink); }

  .offer { position: absolute; background: var(--panel-black); color: var(--white); text-align: center; font-size: 18px; line-height: 26px; padding-top: 5px; }
  .offer em { font-style: normal; color: var(--accent-yellow); font-size: 20px; }

  .photo--frozen { left: 14px; top: 262px; width: 400px; height: 326px; border-radius: 24px;
    background: radial-gradient(ellipse at 30% 55%, #f4c441 0%, #f0b43a 30%, transparent 60%),
                radial-gradient(ellipse at 72% 50%, #f3a9a6 0%, #eaa09a 28%, transparent 55%), var(--white); }
  .photo--juice { left: 652px; top: 282px; width: 196px; height: 312px;
    background: radial-gradient(ellipse at 55% 55%, #ffb21f 0%, #f7a11a 35%, transparent 68%); }
  .photo--mug { left: 34px; top: 940px; width: 222px; height: 256px;
    background: radial-gradient(ellipse at 50% 50%, #e9dccb 0%, #d5bfa5 40%, transparent 70%); }
  .photo--iced-chocolate { left: 250px; top: 720px; width: 190px; height: 476px;
    background: radial-gradient(ellipse at 50% 55%, #5a3a2c 0%, #7a5342 40%, transparent 70%); }
  .photo--iced-latte { left: 512px; top: 820px; width: 290px; height: 340px;
    background: radial-gradient(ellipse at 62% 50%, #e6d3bd 0%, #d8bfa3 35%, transparent 65%),
                radial-gradient(ellipse at 20% 82%, #4a2e1f 0%, transparent 30%); }

  .brand { position: absolute; left: 424px; top: 700px; width: 424px; display: flex; align-items: center; justify-content: center; gap: 14px; color: var(--gold); font-size: 78px; line-height: 1; }
  .brand-dot { width: 22px; height: 22px; border-radius: 50%; background: var(--gold); }
</style>
</head>
<body>
<main class="flyer">
  <div class="quad quad--tl"></div>
  <div class="quad quad--tr"></div>
  <div class="quad quad--bl"></div>
  <div class="quad quad--br"></div>

  <div class="photo photo--frozen" role="img" aria-label="Mango and strawberry frozen fruit drinks with fresh fruit"></div>
  <div class="photo photo--juice" role="img" aria-label="Glass of orange juice with oranges"></div>
  <div class="photo photo--mug" role="img" aria-label="Latte in a glass mug"></div>
  <div class="photo photo--iced-chocolate" role="img" aria-label="Iced chocolate drink topped with cream"></div>
  <div class="photo photo--iced-latte" role="img" aria-label="Tall iced latte with coffee beans"></div>

  <h1><span class="title title--dark">Summer</span><span class="title title--light">Drink</span></h1>

  <h2 class="heading heading--dark" style="left:21px;top:112px;">Frozen Fruit Drinks</h2>
  <div class="price-badge price-badge--gold" style="left:284px;top:81px;">
    <svg viewBox="0 0 100 100"><polygon fill="var(--gold)" points="50,0 55,12 64,3 66,16 77,10 76,23 89,21 84,33 97,35 89,45 100,50 89,55 97,65 84,67 89,79 76,77 77,90 66,84 64,97 55,88 50,100 45,88 36,97 34,84 23,90 24,77 11,79 16,67 3,65 11,55 0,50 11,45 3,35 16,33 11,21 24,23 23,10 34,16 36,3 45,12"/></svg>
    <span>£2.95</span>
  </div>
  <ul class="menu menu--dark" style="left:21px;top:184px;">
    <li>Strawberry and banana</li>
    <li>Pineapple, mango and banana</li>
  </ul>

  <h2 class="heading heading--light" style="left:453px;top:112px;">Fruit Juices</h2>
  <div class="price-badge price-badge--white" style="left:712px;top:81px;">
    <svg viewBox="0 0 100 100"><polygon fill="var(--white)" points="50,0 55,12 64,3 66,16 77,10 76,23 89,21 84,33 97,35 89,45 100,50 89,55 97,65 84,67 89,79 76,77 77,90 66,84 64,97 55,88 50,100 45,88 36,97 34,84 23,90 24,77 11,79 16,67 3,65 11,55 0,50 11,45 3,35 16,33 11,21 24,23 23,10 34,16 36,3 45,12"/></svg>
    <span>£2.95</span>
  </div>
  <ul class="menu menu--light" style="left:453px;top:184px;">
    <li>Orange and carrot</li>
    <li>Orange and pineapple</li>
    <li>Pineapple and apple</li>
    <li>Apple and kiwi</li>
    <li>Carrot and ginger</li>
  </ul>
  <div class="offer" style="left:441px;top:381px;width:207px;height:63px;">Add Mint or Ginger<br>for <em>FREE</em></div>

  <h2 class="heading heading--light" style="left:27px;top:658px;">Iced-Coffees</h2>
  <div class="price-badge price-badge--white" style="left:287px;top:621px;">
    <svg viewBox="0 0 100 100"><polygon fill="var(--white)" points="50,0 55,12 64,3 66,16 77,10 76,23 89,21 84,33 97,35 89,45 100,50 89,55 97,65 84,67 89,79 76,77 77,90 66,84 64,97 55,88 50,100 45,88 36,97 34,84 23,90 24,77 11,79 16,67 3,65 11,55 0,50 11,45 3,35 16,33 11,21 24,23 23,10 34,16 36,3 45,12"/></svg>
    <span>£2.45</span>
  </div>
  <ul class="menu menu--light" style="left:27px;top:729px;">
    <li>Iced Coffee</li>
    <li>Iced Latte</li>
    <li>Iced Chocolate Drink</li>
  </ul>
  <div class="offer" style="left:20px;top:860px;width:208px;height:63px;">Add Syrup Shot<br>for <em>10p</em></div>

  <div class="brand"><span class="brand-dot"></span><span>mielina</span></div>
</main>
</body>
</html>
```